CD-Cover-Design für Musikerin
Zielgruppe
Ich bin Musikerin und gebe Seminare. Zielgruppe sind alle die zu meinen Konzerten und Seminaren kommen.
Aufgabenstellung
künstlerisch und kreativ, verspielt

```html
<!DOCTYPE html>
<html lang="en">
<head>
<meta charset="utf-8">
<title>Lorina and Mael – CD Cover</title>
<link rel="stylesheet" href="https://fonts.googleapis.com/css2?family=Source+Sans+3:wght@400;600&family=Dancing+Script:wght@700&display=swap">
<style>
  :root {
    --magenta: #a3137f;
    --violet: #6c0fa2;
    --gold: #c9a40f;
    --track: #9a1ec2;
    --orange: #ff6a12;
    --amber: #ffb21a;
    --white: #ffffff;
    --paper: #ffffff;
    --shadow: rgba(60, 0, 70, 0.55);
  }
  * { margin: 0; padding: 0; box-sizing: border-box; }
  html, body { width: 1200px; height: 619px; overflow: hidden; background: var(--paper); }
  body { position: relative; font-family: "Source Sans 3", sans-serif; color: var(--white); }

  .panel {
    position: absolute; top: 22px; height: 575px;
    background: linear-gradient(90deg, var(--magenta) 0%, #8e0f92 55%, var(--violet) 100%);
    overflow: hidden;
  }
  .panel--back { left: 24px; width: 574px; }
  .panel--front { left: 600px; width: 576px; }

  .intro {
    position: absolute; top: 22px; left: 0; width: 100%;
    text-align: center; font-size: 12.3px; line-height: 15.2px;
  }
  .highlight { color: var(--gold); font-weight: 600; }

  .mandala {
    position: absolute; border-radius: 50%;
    background: radial-gradient(circle, var(--orange) 0%, #f24e2a 55%, var(--amber) 72%, var(--orange) 86%, rgba(255,106,18,0) 100%);
  }
  .mandala--back { left: 104px; top: 72px; width: 378px; height: 378px; }
  .mandala--front { left: 66px; top: 38px; width: 456px; height: 456px; }

  .tracklist {
    position: absolute; left: 194px; top: 162px; width: 198px; height: 198px;
    border-radius: 50%; background: var(--white);
    list-style: none; display: flex; flex-direction: column; justify-content: center;
    align-items: center; font-weight: 600; font-size: 11.8px; line-height: 15.8px; color: var(--track);
  }
  .tracklist .num { color: var(--gold); }

  .contact {
    position: absolute; top: 455px; left: 0; width: 100%;
    text-align: center; font-size: 11px; line-height: 14px;
  }
  .credits {
    position: absolute; top: 491px; left: 0; width: 100%;
    text-align: center; font-size: 10.4px; line-height: 13.5px;
  }

  .portrait {
    position: absolute; left: 119px; top: 89px; width: 357px; height: 357px;
    border-radius: 50%; border: 2px solid var(--gold);
    background: linear-gradient(160deg, #d8cdf0 0%, #9a84d6 45%, #5a3f9a 100%);
  }

  .title {
    position: absolute; font-family: "Dancing Script", cursive; font-weight: 700;
    color: var(--white); line-height: 1; white-space: nowrap;
    text-shadow: 3px 4px 4px var(--shadow);
  }
  .title--first { left: 100px; top: 262px; font-size: 140px; }
  .title--and { left: 96px; top: 404px; font-size: 62px; }
  .title--second { left: 220px; top: 392px; font-size: 132px; }
</style>
</head>
<body>
  <section class="panel panel--back">
    <p class="intro">
      Music is our means of transport and a direct communication with our essence. We would like<br>
      to take you there with our music. Communicating THIS is our joy. We thank you and enjoy...<br>
      Our music is inspired by the spirit of Oneness. <span class="highlight">Lorina and Mael</span>
    </p>

    <div class="mandala mandala--back" role="img" aria-label="Orange and amber mandala ornament framing the track list"></div>

    <ol class="tracklist">
      <li><span class="num">1.</span> Laisser venir</li>
      <li><span class="num">2.</span> Hari Om Tat</li>
      <li><span class="num">3.</span> Blessings</li>
      <li><span class="num">4.</span> Stille Weite Liebe</li>
      <li><span class="num">5.</span> Trust</li>
      <li><span class="num">6.</span> Shanti</li>
      <li><span class="num">7.</span> Wir sind hier</li>
      <li><span class="num">8.</span> Toward the Dawn</li>
    </ol>

    <p class="contact">
      Feel free to contact us. Booking, concerts and contact on our website:<br>
      <span class="highlight">http://www.LorinaandMael.com / Mail: lorina.music@example.net</span>
    </p>

    <p class="credits">
      All song written by Lorina Vennholt.<br>
      All tracks performed by Lorina on vocals, guitar and harmonium and Mael Soren on his celestial violin.<br>
      Special thanks to: Tobin Reyle for his backing vocals on tracks 7 &amp; 8 and his sarot/sisa performance on track 8.<br>
      Jasper Lindqvist playing the guitar on tracks 4 &amp; 7. / Ravi Morell playing the cajon on tracks 1 &amp; 3.<br>
      Henri Dalcourt @ Quartline Studios for recording and mixdown SONARA all rights reserved Lorina Vennholt
    </p>
  </section>

  <section class="panel panel--front">
    <div class="mandala mandala--front" role="img" aria-label="Orange and amber mandala ornament around the portrait"></div>
    <div class="portrait" role="img" aria-label="Violet-toned portrait of the duo holding a violin and a guitar"></div>
    <h1>
      <span class="title title--first">Lorina</span>
      <span class="title title--and">and</span>
      <span class="title title--second">Mael</span>
    </h1>
  </section>
</body>
</html>
```